design a construction company business card

Design business card around our logo. Card must have all the typical info: name, title, address, phone, email, business name, etc. Somewhere on the card I would like to see our motto "Grounded in trust... Driven by craftsmanship." Consider adding a splash of bright orange to the card to complement the blues and silvers/grays in the logo. We are open to metallic inks, textures, etc. We would like to see options on both light and dark backgrounds. The font in the logo is Euro Technic Extended Regular.

```html
<!DOCTYPE html>
<html lang="en">
<head>
<meta charset="utf-8">
<title>Harlow Building Co. – Business Card Options</title>
<link href="https://fonts.googleapis.com/css2?family=Arimo:ital,wght@0,400;1,400&family=Exo+2:wght@400&family=Questrial&family=Roboto+Condensed:wght@400;700&display=swap" rel="stylesheet">
<style>
  :root {
    --page-bg: #ffffff;
    --ink: #1d1d1f;
    --brand-blue: #2b3a9c;
    --navy: #101d42;
    --steel: #5b5b5d;
    --silver: #d4d4d6;
    --faint: #e7e7e9;
    --orange: #f26522;
    --label-grey: #8a8a8c;
    --card-edge: #8c8c8e;
  }
  * { margin: 0; padding: 0; box-sizing: border-box; }
  html, body { width: 1200px; height: 931px; overflow: hidden; background: var(--page-bg); }
  .sheet { position: relative; width: 1200px; height: 931px; }

  .option-title {
    position: absolute; top: 136px; width: 506px; text-align: center;
    font: 400 40px/1 "Questrial", sans-serif; color: var(--ink);
  }
  .option-title--a { left: 66px; }
  .option-title--b { left: 655px; }

  .side-label {
    position: absolute; font: italic 400 26px/1 "Arimo", sans-serif;
    color: var(--label-grey); transform: rotate(-90deg); transform-origin: center;
    letter-spacing: 1px;
  }
  .side-label--front { left: 597px; top: 315px; }
  .side-label--back { left: 604px; top: 622px; }

  .card {
    position: absolute; width: 506px; height: 289px; overflow: hidden;
    border: 2px solid var(--card-edge);
    box-shadow: 3px 5px 8px rgba(0,0,0,0.28);
  }
  .card--light { background: #ffffff; }
  .card--dark { background: var(--navy); }
  .card--front-a { left: 66px; top: 184px; }
  .card--front-b { left: 655px; top: 184px; }
  .card--back-a { left: 70px; top: 498px; }
  .card--back-b { left: 659px; top: 498px; }

  .brand-name {
    position: absolute; left: 22px; top: 52px;
    font: 400 21px/1.1 "Exo 2", sans-serif; letter-spacing: 2px;
    color: var(--brand-blue);
  }
  .card--dark .brand-name { color: #3a4fc0; }

  .person { position: absolute; left: 283px; top: 60px; width: 160px; text-align: center; }
  .person__name { font: 700 32px/1 "Roboto Condensed", sans-serif; color: var(--ink); white-space: nowrap; }
  .person__title { font: 400 20px/1.2 "Roboto Condensed", sans-serif; color: var(--ink); }
  .card--dark .person__name { color: var(--silver); }
  .card--dark .person__title { color: var(--silver); }

  .contact { position: absolute; left: 18px; }
  .contact__bar {
    position: absolute; left: 28px; width: 234px;
    background: var(--brand-blue); color: #fff;
    font: 400 11.4px/14px "Arimo", sans-serif;
    padding: 4px 0 4px 8px; border-radius: 0 10px 0 0; white-space: nowrap;
  }
  .card--dark .contact__bar { background: var(--steel); }
  .contact__icon { position: absolute; left: 0; width: 34px; height: 34px; }
  .contact--address { top: 147px; }
  .contact--phone { top: 186px; }
  .contact--web { top: 225px; }
  .contact--address .contact__bar, .contact--phone .contact__bar { top: 6px; height: 22px; }
  .contact--web .contact__bar { top: 6px; height: 35px; }

  .back-name {
    position: absolute; left: 0; top: 70px; width: 100%; text-align: center;
    font: 400 54px/1.1 "Exo 2", sans-serif; letter-spacing: 6px;
  }
  .card--back-a .back-name { color: var(--faint); }
  .card--back-b .back-name { color: var(--brand-blue); }

  .motto {
    position: absolute; left: 0; top: 256px; width: 100%; height: 25px; text-align: center;
    font: 400 18px/25px "Exo 2", sans-serif; letter-spacing: 0.5px; white-space: nowrap;
  }
  .card--back-a .motto { background: var(--faint); color: var(--brand-blue); }
  .card--back-b .motto { background: var(--steel); color: #f2f2f2; }
</style>
</head>
<body>
<svg width="0" height="0" style="position:absolute">
  <defs>
    <g id="icon-home">
      <circle cx="17" cy="17" r="15.5" fill="#fff" stroke="#f26522" stroke-width="2.4"/>
      <path d="M7 17 L17 9 L27 17 L24 17 L24 24 L10 24 L10 17 Z" fill="#f26522"/>
    </g>
    <g id="icon-phone">
      <circle cx="17" cy="17" r="15.5" fill="#fff" stroke="#f26522" stroke-width="2.4"/>
      <path d="M11 10 Q9 12 11 17 Q14 23 20 25 Q23 26 24 23 L21 20 L19 21.5 Q15 19 13.5 15 L15 13 Z" fill="#f26522"/>
      <path d="M19 10 Q24 11 25 16 M19 13 Q21.5 13.5 22 16" fill="none" stroke="#f26522" stroke-width="1.2"/>
    </g>
    <g id="icon-globe">
      <circle cx="17" cy="17" r="15.5" fill="#fff" stroke="#f26522" stroke-width="2.4"/>
      <g fill="none" stroke="#f26522" stroke-width="1.3">
        <circle cx="17" cy="17" r="8.5"/>
        <ellipse cx="17" cy="17" rx="3.8" ry="8.5"/>
        <line x1="8.5" y1="17" x2="25.5" y2="17"/>
        <path d="M10 12.5 H24 M10 21.5 H24"/>
      </g>
    </g>
  </defs>
</svg>

<main class="sheet">
  <h2 class="option-title option-title--a">Option A</h2>
  <h2 class="option-title option-title--b">Option B</h2>
  <span class="side-label side-label--front">FRONT</span>
  <span class="side-label side-label--back">BACK</span>

  <!-- Light front -->
  <section class="card card--light card--front-a">
    <div class="brand-name">HARLOW<br>BUILDING CO.</div>
    <div class="person"><div class="person__name">NAME HERE</div><div class="person__title">Title</div></div>
    <div class="contact contact--address">
      <div class="contact__bar">2740 Ridgeline Rd, Dayton, OH 45405</div>
      <svg class="contact__icon" viewBox="0 0 34 34"><use href="#icon-home"/></svg>
    </div>
    <div class="contact contact--phone">
      <div class="contact__bar">Phone: 937.555.0142 • Fax: 937.555.0187</div>
      <svg class="contact__icon" viewBox="0 0 34 34"><use href="#icon-phone"/></svg>
    </div>
    <div class="contact contact--web">
      <div class="contact__bar">email: info@harlowbuildingco.com<br>web: www.harlowbuildingco.com</div>
      <svg class="contact__icon" viewBox="0 0 34 34"><use href="#icon-globe"/></svg>
    </div>
  </section>

  <!-- Dark front -->
  <section class="card card--dark card--front-b">
    <div class="brand-name">HARLOW<br>BUILDING CO.</div>
    <div class="person"><div class="person__name">NAME HERE</div><div class="person__title">Title</div></div>
    <div class="contact contact--address">
      <div class="contact__bar">2740 Ridgeline Rd, Dayton, OH 45405</div>
      <svg class="contact__icon" viewBox="0 0 34 34"><use href="#icon-home"/></svg>
    </div>
    <div class="contact contact--phone">
      <div class="contact__bar">Phone: 937.555.0142 • Fax: 937.555.0187</div>
      <svg class="contact__icon" viewBox="0 0 34 34"><use href="#icon-phone"/></svg>
    </div>
    <div class="contact contact--web">
      <div class="contact__bar">email: info@harlowbuildingco.com<br>web: www.harlowbuildingco.com</div>
      <svg class="contact__icon" viewBox="0 0 34 34"><use href="#icon-globe"/></svg>
    </div>
  </section>

  <!-- Light back -->
  <section class="card card--light card--back-a">
    <div class="back-name">HARLOW<br>BUILDING CO.</div>
    <p class="motto">Grounded in trust... Driven by craftsmanship</p>
  </section>

  <!-- Dark back -->
  <section class="card card--dark card--back-b">
    <div class="back-name">HARLOW<br>BUILDING CO.</div>
    <p class="motto">Grounded in trust... Driven by craftsmanship</p>
  </section>
</main>
</body>
</html>
```